Graphic to hang inside of fitness studio

This graphic will be printed on vinyl and hung inside of a boutique fitness studio for 2019. Graphic should read YEAR OF POSSIBILITIES.

2018 was called Year of Living Well. We would like something on trend for 2019 to hang within the studio as our 2019 Mantra. It is not a logo but for internal use. I've attached our logo here and the website is www.kestrelmovehall.com for additional reference. Thank you.

Target Market(s)

25 to 45 women

Industry/Entity Type

Fitness

Colors

Designer to choose colors to be used in the design.

Requirements
Must have
• On trend for 2019. (no people in image)
• Year of Possibilities in trendy font.
• Easy to read.
• Need text only.
• Do not need graphic images.
Nice to have
• Tintorell colours for 2019
• 2019 design trends for background
Should not have
• Male dominate colour or masculine traits.
• Photos of fitness.
• Photos of people.
• Photos of equipment.

```html
<!DOCTYPE html>
<html lang="en">
<head>
<meta charset="utf-8">
<title>Year of Possibilities</title>
<link rel="stylesheet" href="https://fonts.googleapis.com/css2?family=Anton&family=Allura&display=swap">
<style>
  :root {
    --coral-deep: #f26c5c;
    --coral-soft: #f48a7d;
    --white: #ffffff;
  }
  html, body {
    margin: 0;
    padding: 0;
    width: 849px;
    height: 1200px;
    overflow: hidden;
    background: var(--coral-deep);
  }
  .poster {
    position: relative;
    width: 849px;
    height: 1200px;
    overflow: hidden;
    background: var(--coral-deep);
  }
  .backdrop {
    position: absolute;
    inset: 0;
  }
  .mantra {
    position: absolute;
    left: 0;
    right: 0;
    margin: 0;
    color: var(--white);
    font-weight: 400;
    text-align: center;
    line-height: 1;
    white-space: nowrap;
  }
  .mantra-year {
    top: 108px;
    font-family: "Anton", sans-serif;
    font-size: 236px;
    letter-spacing: 0;
    padding-left: 4px;
    transform: scaleY(1.26);
    transform-origin: center top;
  }
  .mantra-of {
    top: 492px;
    font-family: "Anton", sans-serif;
    font-size: 172px;
    letter-spacing: 26px;
    padding-left: 26px;
  }
  .mantra-possibilities {
    top: 735px;
    font-family: "Allura", cursive;
    font-size: 172px;
    padding-left: 6px;
  }
</style>
</head>
<body>
<main class="poster">
  <svg class="backdrop" width="849" height="1200" viewBox="0 0 849 1200" aria-hidden="true">
    <polygon class="band-soft" points="0,600 849,930 849,940 560,1200 0,1200" fill="var(--coral-soft)"/>
    <g class="frame" stroke="var(--white)" stroke-width="4" fill="none">
      <line x1="147" y1="175" x2="200" y2="175"/>
      <line x1="655" y1="175" x2="730" y2="175"/>
      <line x1="147" y1="175" x2="147" y2="755"/>
      <line x1="147" y1="905" x2="147" y2="1090"/>
      <line x1="730" y1="175" x2="730" y2="735"/>
      <line x1="730" y1="915" x2="730" y2="1090"/>
      <line x1="147" y1="1090" x2="730" y2="1090"/>
    </g>
  </svg>
  <h1 class="mantra mantra-year">YEAR</h1>
  <p class="mantra mantra-of">OF</p>
  <svg class="backdrop" width="849" height="1200" viewBox="0 0 849 1200" aria-hidden="true">
    <polygon class="shard" points="0,85 370,580 0,695" fill="var(--white)"/>
  </svg>
  <p class="mantra mantra-possibilities">possibilities</p>
</main>
</body>
</html>
```